GLS biz card

We need a business card design for our new company based in Los Angeles called "Gold Lantern Studios". We develop film and television projects. We work with investors, financiers, film production companies, film distribution and sales companies as well as studios. We would like to incorporate our logo (see attached) on a two-sided card. We need to include: name and title, address, phone, email and company website.

Target Market(s)

Business, financial and studio clients

Industry/Entity Type

Business

Contact Information for Business Card

Two-sided. We are thinking of the logo on one side and the information on the back. Please feel free to be creative! Thanks.

Requirements
Must have
• Please include the following text information, excluding the "CAPS CATEGORY:" and please allow the ability for us to change the name, title and email address for each company employee):
• NAME & TITLE:
• Peter Dunmore
• Managing Partner
• COMPANY NAME:
• GOLD LANTERN STUDIOS (please use existing logo)
• COMPANY ADDRESS:
• KVT Arts Park
• 2480 Wexley Boulevard
• Arts Hall, 4th Floor
• Manhattan Beach, CA 90266
• COMPANY PHONE NUMBER:
• 310-555-4206
• COMPANY WEBSITE ADDRESS:
• www.goldlanternstudioshouse.com
• EMAIL ADDRESS: (only one per card)
• frank@goldlanternstudioshouse.com
• tizzy@goldlanternstudioshouse.com
• peter@goldlanternstudioshouse.com

```html
<!DOCTYPE html>
<html lang="en">
<head>
<meta charset="utf-8">
<title>Gold Lantern Studios — Business Card</title>
<link rel="stylesheet" href="https://fonts.googleapis.com/css2?family=Lato:wght@400;700;900&display=swap">
<style>
  :root {
    --backdrop: #3b3d40;
    --card: #0c0f15;
    --card-edge: #151a22;
    --accent: #19b8e6;
    --ink: #e6edf2;
  }
  * { box-sizing: border-box; margin: 0; padding: 0; }
  html, body {
    width: 1200px; height: 926px; overflow: hidden;
    background: var(--backdrop);
    font-family: "Lato", Arial, sans-serif;
  }
  .sheet {
    width: 1200px; height: 926px;
    display: flex; flex-direction: column; align-items: center; justify-content: center;
    gap: 40px;
  }
  .card {
    position: relative;
    width: 700px; height: 400px;
    background: radial-gradient(ellipse at 40% 30%, var(--card-edge) 0%, var(--card) 70%);
    box-shadow: 0 10px 30px rgba(0,0,0,.45);
    overflow: hidden;
  }

  /* Shared brand lockup */
  .brand { display: flex; flex-direction: column; align-items: center; }
  .brand__mark { border-radius: 50%; background: var(--accent); }
  .brand__name { font-weight: 900; color: var(--accent); white-space: nowrap; }

  /* Front side */
  .card--front .brand { position: absolute; left: 0; right: 0; top: 92px; }
  .card--front .brand__mark { width: 120px; height: 120px; }
  .card--front .brand__name { margin-top: 30px; font-size: 34px; letter-spacing: 3px; }

  /* Back side */
  .card--back .brand { position: absolute; left: 56px; top: 40px; }
  .card--back .brand__mark { width: 64px; height: 64px; }
  .card--back .brand__name { margin-top: 14px; font-size: 15px; letter-spacing: 1.5px; }

  .person { position: absolute; right: 44px; top: 84px; text-align: right; }
  .person__name { font-size: 30px; font-weight: 400; color: var(--accent); white-space: nowrap; }
  .person__name strong { font-weight: 700; }
  .person__title { margin-top: 2px; font-size: 14px; letter-spacing: .5px; color: var(--accent); text-transform: uppercase; }

  .contact {
    position: absolute; left: 60px; right: 40px; bottom: 40px;
    list-style: none;
    font-size: 16px; color: var(--ink); letter-spacing: .3px;
  }
  .contact__item { display: flex; align-items: flex-start; gap: 10px; line-height: 27px; }
  .contact__icon { width: 14px; height: 14px; margin-top: 6px; fill: var(--accent); flex: none; }
  .contact__icon--stroke { fill: none; stroke: var(--accent); stroke-width: 2; }
</style>
</head>
<body>
<main class="sheet">

  <section class="card card--front" aria-label="Card front">
    <div class="brand">
      <div class="brand__mark"></div>
      <div class="brand__name">GOLD LANTERN STUDIOS</div>
    </div>
  </section>

  <section class="card card--back" aria-label="Card back">
    <div class="brand">
      <div class="brand__mark"></div>
      <div class="brand__name">GOLD LANTERN STUDIOS</div>
    </div>

    <div class="person">
      <div class="person__name">Peter <strong>Dunmore</strong></div>
      <div class="person__title">Managing Partner</div>
    </div>

    <ul class="contact">
      <li class="contact__item">
        <svg class="contact__icon" viewBox="0 0 16 16"><path d="M3 1l3 3-1.5 2c1 2 3 4 5 5L11.5 9.5l3 3-2 2.5C7 14.5 1.5 9 1 3.5z"/></svg>
        <span>310-555-4206</span>
      </li>
      <li class="contact__item">
        <svg class="contact__icon contact__icon--stroke" viewBox="0 0 16 16"><path d="M7 9l2-2M6 7L4 9a2 2 0 003 3l2-2M10 9l2-2a2 2 0 00-3-3L7 6"/></svg>
        <span>www.goldlanternstudioshouse.com</span>
      </li>
      <li class="contact__item">
        <svg class="contact__icon" viewBox="0 0 16 16"><path d="M1 3h14v10H1z"/><path d="M1 3l7 6 7-6" fill="none" stroke="#0c0f15" stroke-width="1.4"/></svg>
        <span>peter@goldlanternstudioshouse.com</span>
      </li>
      <li class="contact__item">
        <svg class="contact__icon" viewBox="0 0 16 16"><path d="M8 1l7 7h-2v7H9.5v-4h-3v4H3V8H1z"/></svg>
        <span>KVT Arts Park, 2480 Wexley Boulevard, Arts Hall, 4th Floor<br>Manhattan Beach, CA 90266</span>
      </li>
    </ul>
  </section>

</main>
</body>
</html>
```